Business card for a "family office" company

Please provide professional looking business card designs, incorporating the attached logo and below details. Harrowmere Holdings Pty Ltd is a family office / financial investment company. We are looking for a modern, professional and contemporary card design.

Industry/Entity Type

Finance

Contact Information for Business Card

Name: Dean Mollick
Title: Director
Company: Harrowmere Holdings Pty Ltd
Email: harrowdean@quillnet.example
Mobile: 0462 735 418
Address: 4/312 Barnaby Parade, Wrenhaven WA 6190, Australia

Requirements
Must have
• All details above and the logo. logo only on back side. incorporate colours of logo
Nice to have
• up to you
Should not have
• ?

```html
<!DOCTYPE html>
<html lang="en">
<head>
<meta charset="utf-8">
<title>Harrowmere Holdings – Business Card</title>
<link href="https://fonts.googleapis.com/css2?family=Cinzel:wght@400;600&family=Jost:wght@400&display=swap" rel="stylesheet">
<style>
  :root {
    --navy: #26256a;
    --paper: #ffffff;
    --backdrop: #3b3b3d;
    --ink-soft: #2e2e38;
  }
  * { box-sizing: border-box; margin: 0; padding: 0; }
  html, body {
    width: 1200px; height: 1000px; overflow: hidden;
    background: var(--backdrop);
  }
  .card {
    position: absolute; left: 204px;
    width: 792px; height: 440px;
    background: var(--paper);
    box-shadow: 0 12px 30px rgba(0,0,0,.45);
    overflow: hidden;
  }
  .card--front { top: 40px; }
  .card--back { top: 520px; }

  .wordmark {
    position: absolute;
    display: flex; align-items: center; gap: 14px;
    color: var(--navy);
    font-family: "Cinzel", serif; font-weight: 600;
  }
  .wordmark__square {
    width: 34px; height: 34px; background: var(--navy); flex: none;
  }
  .wordmark__text { display: flex; flex-direction: column; align-items: center; line-height: 1; }
  .wordmark__name { font-size: 34px; letter-spacing: 2px; }
  .wordmark__sub { font-size: 13px; letter-spacing: 7px; margin-top: 6px; }

  .card--front .wordmark { left: 50%; top: 150px; transform: translateX(-42%); }

  .card--back .wordmark { right: 40px; top: 60px; }
  .card--back .wordmark__name { font-size: 30px; }
  .card--back .wordmark__sub { font-size: 12px; }

  .contact {
    position: absolute; right: 40px; top: 190px;
    font-family: "Jost", sans-serif; font-size: 17px; letter-spacing: 1px;
    color: var(--ink-soft); text-align: right; line-height: 1.45;
  }
  .contact__row { display: flex; justify-content: flex-end; align-items: center; gap: 12px; }
  .contact__icon { width: 14px; height: 14px; fill: var(--navy); flex: none; }
  .contact__address { margin-top: 26px; padding-right: 26px; }

  .person {
    position: absolute; left: 0; bottom: 70px;
    display: flex; align-items: stretch; gap: 20px;
  }
  .person__bar { width: 14px; background: var(--navy); }
  .person__name {
    font-family: "Cinzel", serif; font-weight: 600; font-size: 32px;
    color: var(--navy); letter-spacing: 1px; line-height: 1;
  }
  .person__title {
    font-family: "Cinzel", serif; font-weight: 600; font-size: 16px;
    color: var(--ink-soft); letter-spacing: 1px; margin-top: 4px;
  }
</style>
</head>
<body>
  <section class="card card--front">
    <div class="wordmark">
      <span class="wordmark__square"></span>
      <span class="wordmark__text">
        <span class="wordmark__name">HARROWMERE</span>
        <span class="wordmark__sub">HOLDINGS</span>
      </span>
    </div>
  </section>

  <section class="card card--back">
    <div class="wordmark">
      <span class="wordmark__square"></span>
      <span class="wordmark__text">
        <span class="wordmark__name">HARROWMERE</span>
        <span class="wordmark__sub">HOLDINGS</span>
      </span>
    </div>

    <div class="contact">
      <div class="contact__row">0462 735 418
        <svg class="contact__icon" viewBox="0 0 16 16" aria-hidden="true"><path d="M3 1h3l1 4-2 1a9 9 0 0 0 5 5l1-2 4 1v3a2 2 0 0 1-2 2A13 13 0 0 1 1 3a2 2 0 0 1 2-2z"/></svg>
      </div>
      <div class="contact__row">harrowdean@quillnet.example
        <svg class="contact__icon" viewBox="0 0 16 16" aria-hidden="true"><path d="M1 3h14v10H1z"/><path d="M1.5 3.5l6.5 5.5 6.5-5.5" fill="none" stroke="#fff" stroke-width="1.2"/></svg>
      </div>
      <div class="contact__row">www.harrowmere.example
        <svg class="contact__icon" viewBox="0 0 16 16" aria-hidden="true"><circle cx="8" cy="8" r="7"/><path d="M1 8h14M8 1v14M3 4h10M3 12h10" stroke="#fff" stroke-width="1" fill="none"/></svg>
      </div>
      <div class="contact__address">4/312 Barnaby Parade,<br>Wrenhaven WA 6190, Australia</div>
    </div>

    <div class="person">
      <span class="person__bar"></span>
      <div>
        <div class="person__name">DEAN MOLLICK</div>
        <div class="person__title">Director</div>
      </div>
    </div>
  </section>
</body>
</html>
```